Buchcover-Design für Fragenbuch
Ganz herzlichen Dank. Die Zusammenarbeit war völlig reibungslos und entspannt. Änderungswünsche wurden professionell umgesetzt und die kreativen Vorschläge fand ich super. Ich bin total glücklich mit dem Ergebnis.
Zielgruppe
Autorin und Workshopleiterin. Zielgruppe: Frauen ab 30
Aufgabenstellung
Ich benötige ein komplettes Buchcover, sowie 12 farbige Innenseiten. Es geht um ein Fragenbuch zum Ausfüllen mit dem Titel:
„Finde zurück zur leisen Mitte
Ein Arbeitsheft zum Eintragen für tiefere seelische Ruhe“
Das Format des Buches beträgt 17x22cm. Es ist in 12 Wochen unterteilt. Darum hätte ich gerne zwischen den einzelnen Wochen eine farbige Seite (1. Woche, 2. Woche etc.), die designmäßig mit dem Außencover korrespondiert.
Die Farben sollten eher zart oder gedeckt sein. Auf keinen Fall jedoch kitschig. Wichtig ist mir, dass keine bestimmte Person zu sehen ist. (Foto)
Das ist meine Website www.finde-zurueck-zur-leisen-mitte.de

```html
<!DOCTYPE html>
<html lang="de">
<head>
<meta charset="utf-8">
<title>Finde zurück zur leisen Mitte – Cover und Wochenseite</title>
<link rel="stylesheet" href="https://fonts.googleapis.com/css2?family=EB+Garamond:wght@400;500&family=Mrs+Saint+Delafield&display=swap">
<style>
  :root {
    --sand: #dbcdc4;
    --taupe: #b3a9a4;
    --paper: #ffffff;
    --ink: #121010;
    --wine: #7a2d28;
    --backdrop: #ffffff;
    --photo-light: #f7f4f2;
    --photo-warm: #ebe2dc;
    --still-light: #ececec;
    --still-mid: #dcdcdc;
  }
  * { margin: 0; padding: 0; box-sizing: border-box; }
  html, body {
    width: 1200px; height: 849px; overflow: hidden;
    background: var(--backdrop);
  }
  .stage {
    position: absolute; top: 0; left: 0;
    width: 1754px; height: 1240px;
    transform: scale(0.68415);
    transform-origin: 0 0;
    font-family: "EB Garamond", Georgia, serif;
  }
  .page {
    position: absolute; top: 269px;
    width: 529px; height: 684px;
    background: var(--sand);
    overflow: hidden;
  }
  .page--cover { left: 340px; }
  .page--week { left: 970px; }
  .page__band {
    position: absolute; left: 0; top: 472px;
    width: 100%; height: 212px;
    background: var(--taupe);
  }

  /* cover */
  .cover__photo {
    position: absolute; left: 74px; top: 0;
    width: 384px; height: 399px;
    border-radius: 0 0 175px 175px;
    background: linear-gradient(150deg, var(--photo-light) 30%, var(--photo-warm) 100%);
  }
  .cover__title {
    position: absolute; right: 66px; top: 322px;
    text-align: right;
    font-size: 44px; font-weight: 400;
    line-height: 54px; letter-spacing: 0.5px;
    color: var(--ink);
  }
  .cover__subtitle {
    position: absolute; right: 76px; top: 478px;
    font-size: 39px; font-weight: 400;
    color: var(--paper);
    line-height: 1;
  }
  .cover__tagline {
    position: absolute; left: 94px; top: 547px;
    width: 364px; height: 43px;
    background: var(--sand);
    display: flex; align-items: center; justify-content: center;
    font-size: 12px; letter-spacing: 0.1px;
    color: var(--paper); text-transform: uppercase;
  }
  .cover__author {
    position: absolute; left: 0; top: 605px;
    width: 100%; text-align: center;
    padding-left: 30px;
    font-family: "Mrs Saint Delafield", cursive;
    font-size: 36px; color: var(--wine);
  }

  /* week divider */
  .week__tab {
    position: absolute; left: 141px; top: 0;
    width: 235px; height: 247px;
    border-radius: 0 0 100px 100px;
    background: var(--paper);
    text-align: center; color: var(--ink);
  }
  .week__number {
    display: block; margin-top: 40px;
    font-size: 76px; line-height: 72px;
  }
  .week__label {
    display: block; margin-top: 0;
    font-size: 50px; line-height: 56px; letter-spacing: 1px;
  }
  .week__headline {
    position: absolute; left: 108px; top: 323px;
    width: 330px; text-align: center;
    font-size: 30px; line-height: 37px;
    color: var(--ink); letter-spacing: 0.3px;
  }
  .week__section {
    position: absolute; left: 0; top: 485px;
    width: 528px; text-align: center;
    font-size: 11px; color: var(--paper);
    text-transform: uppercase;
  }
  .week__arch {
    position: absolute; left: 310px; top: 488px;
    width: 218px; height: 196px;
    border-radius: 105px 105px 0 0;
    background: var(--paper);
  }
  .week__still {
    position: absolute; left: 20px; top: 30px;
    width: 178px; height: 166px;
    border-radius: 89px 89px 0 0;
    background: linear-gradient(180deg, var(--still-light), var(--still-mid));
  }
</style>
</head>
<body>
<div class="stage">
  <section class="page page--cover">
    <div class="page__band"></div>
    <div class="cover__photo" role="img" aria-label="Foto: aufgeschlagener Jahresplaner und roségoldener Kugelschreiber auf weißem Tisch"></div>
    <h1 class="cover__title">FINDE ZURÜCK<br>ZUR LEISEN<br>MITTE</h1>
    <p class="cover__subtitle">Ein Arbeitsheft</p>
    <p class="cover__tagline">Zum Eintragen für tiefere seelische Ruhe</p>
    <p class="cover__author">by Mira Helling</p>
  </section>

  <section class="page page--week">
    <div class="page__band"></div>
    <div class="week__tab">
      <span class="week__number">1</span>
      <span class="week__label">WOCHE</span>
    </div>
    <h2 class="week__headline">YOUR MODULE<br>HEADLINE COMES<br>TO HERE</h2>
    <p class="week__section">Section Headline</p>
    <div class="week__arch">
      <div class="week__still" role="img" aria-label="Foto: goldener Apfel schwebt über einer weißen Skulpturhand vor hellgrauem Grund"></div>
    </div>
  </section>
</div>
</body>
</html>
```